Vermilion Reel Works Web Design

COMPANY: VERMILION REEL WORKS
LOCATION: SHANGHAI, CHINA
AREA: FILM/TV DRAMA/COMMERCIALS/GAME POST PRODUCTION, SOUND DESIGN, MUSIC, and GAME.
WEB STYLE: SIMPLE, PROFESSIONAL, TRUSTWORTHY

LANGUAGE: ENGLISH, CHINESE. (Same layout, different language)
UPDATE: AFTER PROJECT FINISHED, WE NEED UPDATE BY OURSELVES.

MAIN SUBJECT: 6
1 HOMEPAGE
2 ABOUT US
3 TEAM
4 SERVICES
5 FACILITY
6 CONTACT

add one page of JOB OPPORTUNITIES.

DETAILS
1 HOMEPAGE
SLOGAN: Vermilion Reel Works provides a well-designed working environment which amplifies your team’s ability to reach their creative goals.

Our services include:
 Feature Films
 Music & Scoring
 Commercials
 ADR & Foley
 Sound & Picture Editorial
 Sound Design
 Video Game

2 ABOUT US
Vermilion Reel Works is located in the premiere South-Bund area of Shanghai. Occupying a 5000 square meter Technical Building, Vermilion Reel Works was built by a filmmaker for filmmakers, and is one of the largest, most versatile full-service post-production facilities in China.

Vermilion Reel Works is positioning to be at the forefront of the latest technology. Our goal is to provide a comprehensive solution for the post-production needs of our clients. We offer two fully-equipped dubbing stages (one of which will be certified KESTRON VOXAR PREMIERE), a large variety of both picture and sound editing rooms, impressive Foley and ADR stages, a world-class scoring stage, and complete audio and video transfer services.

We can handle your entire project from editing all the way to the end of the final sound mix; all under one extremely comfortable roof. We fully realize that the true art is in listening to the needs of our clients and making their greatest vision a reality. To this end our creative team's expertise, with a network of sound supervisors, editors and mixers, will deliver the magic you need. Producers and directors will also find our richly appointed guest accommodations to be a comfortable and soothing place to wind up the day. Every aspect of your project will be taken care of by a skilled and dedicated team, in the way that is best suited to you.

3 TEAM
(attachment 01)

4 SERVICES
Sound Mix
ADR
FOLEY
MUSIC
Sound Design
Sound Edit
Picture Edit
for all the Films, TV Drama, Commercials, Video Games, Online Media
(attachment 02, use photo)

5 FACILITY
(attachment 03)

6 CONTACT
(attachment04)
with map

Project Deadline Extended
Reason: Designers work are great, my bosses will spend 1-2 days select one of these web design, and spend 1-2 days to make some change, maybe use new photos.

```html
<!DOCTYPE html>
<html lang="en">
<head>
<meta charset="utf-8">
<title>Vermilion Reel Works — Team</title>
<link rel="stylesheet" href="https://fonts.googleapis.com/css2?family=Oswald:wght@500&family=Montserrat:ital,wght@0,400;0,700;1,400&display=swap">
<style>
  :root {
    --studio-dark: #0b0a09;
    --studio-warm: #3a2c18;
    --band-blue: #1f6fa6;
    --band-blue-deep: #175a8a;
    --band-blue-light: #2c86c0;
    --text-main: #ffffff;
    --text-soft: #e8e8e8;
    --nav-track: #8a8a8a;
    --nav-active: #2f8fd0;
    --ring: #ffffff;
  }
  * { margin: 0; padding: 0; box-sizing: border-box; }
  html, body { width: 1200px; height: 600px; overflow: hidden; background: var(--studio-dark); }
  .page {
    position: relative; width: 1200px; height: 600px; overflow: hidden;
    font-family: "Montserrat", sans-serif; color: var(--text-main);
  }
  .studio-backdrop {
    position: absolute; inset: 0;
    background:
      radial-gradient(ellipse 420px 260px at 600px 230px, #2a2520 0%, transparent 70%),
      radial-gradient(ellipse 500px 300px at 800px 520px, var(--studio-warm) 0%, transparent 75%),
      radial-gradient(ellipse 300px 260px at 1080px 280px, #3b3a38 0%, transparent 70%),
      linear-gradient(180deg, #141210 0%, #1a150e 60%, #231a0e 100%);
  }
  .decor { position: absolute; inset: 0; }
  .menu-toggle { position: absolute; left: 247px; top: 23px; width: 19px; height: 14px; }
  .section-nav { position: absolute; left: 1008px; top: 10px; width: 180px; }
  .section-nav .track { position: absolute; left: 0; top: 0; width: 180px; height: 2px; background: var(--nav-track); }
  .section-nav .track-active { position: absolute; left: 64px; top: 0; width: 28px; height: 2px; background: var(--nav-active); }
  .section-nav ol { list-style: none; position: relative; top: 6px; height: 12px; }
  .section-nav li { position: absolute; font-size: 9.5px; color: var(--text-soft); transform: translateX(-50%); }
  .section-title {
    position: absolute; left: 365px; top: 152px;
    font-family: "Oswald", sans-serif; font-weight: 500; font-size: 32px; letter-spacing: 0.5px;
    line-height: 1; transform: scaleY(1.08);
  }
  .member { position: absolute; top: 224px; width: 300px; }
  .member-one { left: 351px; }
  .member-two { left: 676px; width: 330px; }
  .portrait {
    width: 98px; height: 98px; border-radius: 50%;
    border: 2px solid var(--ring);
    box-shadow: 0 0 0 4px rgba(0,0,0,0.55);
    background: radial-gradient(circle at 50% 40%, #c9a88e 0%, #8e7360 45%, #4a5a3f 100%);
  }
  .member-one .portrait { margin-left: -2px; }
  .member-two .portrait { margin-left: 2px; margin-top: 4px; background: radial-gradient(circle at 50% 40%, #caa897 0%, #8a7668 45%, #3e5a32 100%); }
  .member-name { font-weight: 700; font-size: 10.6px; margin-top: 32px; letter-spacing: 0.1px; }
  .member-two .member-name { margin-top: 28px; }
  .member-bio { font-size: 9.4px; line-height: 12px; margin-top: 14px; color: var(--text-soft); }
  .member-credits { font-style: italic; margin-top: 12px; }
  .next-arrow { position: absolute; left: 1134px; top: 284px; width: 18px; height: 40px; }
</style>
</head>
<body>
<main class="page">
  <div class="studio-backdrop" role="img" aria-label="Dimly lit sound studio with a mixing console, keyboard and coffee mug on a wooden desk"></div>

  <svg class="decor" width="1200" height="600" viewBox="0 0 1200 600" aria-hidden="true">
    <polygon points="0,0 428,0 84,600 0,600" fill="var(--band-blue)" opacity="0.92"/>
    <polygon points="0,0 312,0 0,540" fill="var(--band-blue-deep)" opacity="0.55"/>
    <polygon points="1200,264 1200,600 1016,600" fill="var(--band-blue-light)" opacity="0.85"/>
    <polygon points="1200,380 1200,600 1088,600" fill="var(--band-blue)" opacity="0.5"/>
    <g stroke="#ffffff" stroke-opacity="0.18" stroke-width="0.8" fill="none">
      <line x1="300" y1="0" x2="980" y2="600"/>
      <line x1="680" y1="0" x2="1000" y2="600"/>
      <line x1="0" y1="420" x2="1200" y2="90"/>
      <line x1="250" y1="600" x2="1200" y2="170"/>
      <line x1="560" y1="0" x2="820" y2="600"/>
      <line x1="0" y1="180" x2="1200" y2="260"/>
      <line x1="780" y1="0" x2="1200" y2="600"/>
    </g>
  </svg>

  <svg class="menu-toggle" viewBox="0 0 19 14" aria-label="Menu">
    <g fill="#ffffff">
      <rect y="0" width="19" height="1.6"/><rect y="3.1" width="19" height="1.6"/>
      <rect y="6.2" width="19" height="1.6"/><rect y="9.3" width="19" height="1.6"/>
      <rect y="12.4" width="19" height="1.6"/>
    </g>
  </svg>

  <nav class="section-nav" aria-label="Sections">
    <div class="track"></div><div class="track-active"></div>
    <ol>
      <li style="left:26px">01</li><li style="left:57px">02</li><li style="left:87px">03</li>
      <li style="left:117px">04</li><li style="left:146px">05</li><li style="left:175px">06</li>
    </ol>
  </nav>

  <h1 class="section-title">TEAM</h1>

  <article class="member member-one">
    <div class="portrait" role="img" aria-label="Portrait photo of Lena Zhou"></div>
    <h2 class="member-name">LENA ZHOU – CEO/Co-Founder / Producer</h2>
    <p class="member-bio">Lena is the co-founder of Vermilion Reel Works and a 15 year veteran in the film industry. She is an accomplished producer who has been involved in co-productions both locally in Asia and internationally. She has developed and implemented several outstanding film projects whilst acting as the sole representative of the renowned European producer Dario Valenti in Asia.</p>
    <p class="member-bio member-credits">Northline China Part; La Luna Sottile(Italy); Two Cranes(Italy); Q-19(Japan); Vision Harbor by Marco Bellandi.</p>
  </article>

  <article class="member member-two">
    <div class="portrait" role="img" aria-label="Portrait photo of Rowan Fairley"></div>
    <h2 class="member-name">ROWAN FAIRLEY – Re-Recording Mixer / REELDB#：nm0418273</h2>
    <p class="member-bio">Aurora Awards – nominated / Outstanding Sound Mixing for a Mini-series or a Movie<br>
    Iron Orchard (2007)<br>
    Meridian Awards – Nominated /Best Sound in a Dramatic Program<br>
    Deltaland (2010)<br>
    Cascade Awards / Best Overall Sound in a Motion Picture<br>
    Siege on Harbor Street (2013)</p>
  </article>

  <svg class="next-arrow" viewBox="0 0 18 40" aria-label="Next section">
    <polyline points="2,2 16,20 2,38" fill="none" stroke="#e6e6e6" stroke-width="2"/>
  </svg>
</main>
</body>
</html>
```